Video Editing Website - Wordpress Design Project

Hi There
I am setting up a Tribute Funeral Video and Home Video Editing Website for my Company. "Reel Keepsake". This is to assist people with putting together their Videos and Photos with music to show at a Funeral or for Family Memories. I already have a domain www.reelkeepsake.com.au, but I have no host yet.

Some websites that already do this are http://www.lanternclips.com.au/tributes, http://www.hearthfilmcraft.com.au/services/funeral-tribute-videos.html, and http://www.quillmontage.com.au/
These are examples not to cpy, but to get an idea of what I am offering so you can design accordingly.

I have a logo which is attached. You will see that the logo is mainly blue, so I would appreciate a website with that colour on the pages, but not ALL over the page.

I would like to upload videos occasionally from flickstow.com so I would appreciate that option incorporated.

Thank you lots.
Callum

Target Market(s)

Families predominately in the 25-60 age range

Industry/Entity Type

It Company

Requirements
Must have
• *Ability to upload Videos from flickstow.com
*Ability for me to edit the content whenever I need to
*A contact page to send email messages to me

```html
<!DOCTYPE html>
<html lang="en">
<head>
<meta charset="utf-8">
<title>Reel Keepsake</title>
<link href="https://fonts.googleapis.com/css2?family=Questrial&family=Oswald:wght@300&family=Teko:wght@600&display=swap" rel="stylesheet">
<style>
:root{
  --blue:#2458b0;
  --ink:#333;
  --grey:#f1f1f1;
  --mid:#8a8a8a;
  --line:#cfcfcf;
  --white:#fff;
}
*{box-sizing:border-box;margin:0;padding:0}
html,body{width:784px;height:1200px;overflow:hidden;background:var(--white)}
body{position:relative;font-family:Arial,Helvetica,sans-serif;color:var(--ink)}
.abs{position:absolute}
.header-top{left:0;top:0;width:784px;height:50px;background:linear-gradient(#fff,#ececec)}
.hero-art{left:0;top:0}
.logo{left:6px;top:0;width:102px;height:82px;background:var(--white);border-radius:0 0 6px 6px;box-shadow:0 1px 4px rgba(0,0,0,.25);display:flex;align-items:center;justify-content:center;gap:4px;flex-direction:column}
.logo-mark{width:22px;height:22px;background:var(--blue);border-radius:50%}
.logo-name{font-family:Questrial,sans-serif;font-size:13px;color:var(--blue)}
.social{top:19px;display:flex;gap:7px;right:16px}
.social span{width:22px;height:22px;border-radius:50%;background:#222;display:block}
.nav{left:128px;top:61px;display:flex;font-family:Questrial,sans-serif;font-size:14px;color:var(--white)}
.nav a{color:inherit;text-decoration:none;margin-right:35px}
.tagline{left:0;top:356px;width:784px;text-align:center;font-family:Questrial,sans-serif;font-size:21px;line-height:25px;color:#222;font-weight:400}
.intro{left:15px;top:425px;width:750px;font-size:9.6px;line-height:12px;color:#444}
.occasions{left:0;top:482px;width:784px;height:310px;background:var(--grey);border-top:1px solid #e4e4e4;border-bottom:1px solid #e4e4e4}
.section-title{font-family:Teko,sans-serif;font-weight:600;color:var(--blue);letter-spacing:.5px;text-transform:uppercase}
.occasions .section-title{position:absolute;left:27px;top:20px;font-size:27px;line-height:30px}
.card{position:absolute;top:58px;width:176px}
.card .photo{width:175px;height:122px;border:5px solid #111;border-radius:3px}
.card h3{font-family:Oswald,sans-serif;font-weight:300;font-size:20px;color:#222;margin-top:8px;line-height:24px}
.card p{font-size:9.6px;line-height:11.6px;color:#444;margin-top:3px;height:46px;width:172px}
.inquire{display:inline-block;margin-top:6px;background:var(--blue);color:var(--white);font-size:8.5px;font-weight:bold;padding:4px 0;border-radius:2px;width:54px;text-align:center}
.testimonials{left:27px;top:824px;width:260px}
.news{left:400px;top:824px;width:330px}
.testimonials .section-title,.news .section-title{font-size:24px;line-height:26px}
.quote{position:relative;margin-top:18px;font-size:9.6px;line-height:11.6px;color:#555}
.quote .lead{padding-left:54px;min-height:28px}
.quote .icon{position:absolute;left:4px;top:0}
.quote .body{margin-top:8px;padding-left:5px}
.quote .by{margin-top:8px;padding-left:5px;color:var(--blue);font-size:8.5px}
.quote-rule{margin:14px 0 0 5px;border-top:1px dotted var(--line);width:240px}
.news-item{position:relative;height:88px}
.news-list{margin-top:12px}
.date{position:absolute;left:0;top:4px;width:43px;text-align:center}
.date b{display:block;height:28px;background:var(--mid);color:var(--white);font-family:Teko,sans-serif;font-size:25px;line-height:31px;border-radius:3px}
.date small{display:block;margin-top:5px;font-size:9.5px;font-weight:bold;color:#555;letter-spacing:.5px}
.news-body{position:absolute;left:54px;top:0;width:272px;font-size:9.6px;line-height:11.6px;color:#555}
.news-body h4{font-size:11px;color:#444;margin-bottom:4px}
.news-body .more{display:block;margin-top:6px;color:var(--blue);font-size:8.5px}
.news-item::after{content:"";position:absolute;left:55px;top:70px;width:272px;border-top:1px solid var(--line)}
.footer{left:0;top:1138px;width:784px;height:62px;background:var(--blue);color:var(--white);text-align:center}
.footer .links{margin-top:18px;font-size:10px}
.footer .copy{margin-top:6px;font-size:8px;color:#dbe4f5}
</style>
</head>
<body>
<div class="abs header-top"></div>

<svg class="abs hero-art" width="784" height="355" viewBox="0 0 784 355">
  <defs>
    <linearGradient id="screen" x1="0" y1="0" x2="1" y2="1">
      <stop offset="0" stop-color="#1e1a18"/><stop offset=".55" stop-color="#6b3b22"/><stop offset="1" stop-color="#2a211c"/>
    </linearGradient>
    <linearGradient id="stripLeft" x1="0" y1="0" x2="1" y2="0">
      <stop offset="0" stop-color="#8f878a"/><stop offset="1" stop-color="#2a2a2a"/>
    </linearGradient>
    <linearGradient id="stripRight" x1="0" y1="0" x2="1" y2="0">
      <stop offset="0" stop-color="#2a2a2a"/><stop offset="1" stop-color="#a8644c"/>
    </linearGradient>
  </defs>
  <path d="M0 50 H784 V128 Q392 52 0 128 Z" fill="var(--blue)"/>
  <line x1="0" y1="51" x2="784" y2="51" stroke="#fff" stroke-width="1.5"/>
  <polygon points="0,134 166,146 166,291 0,282" fill="url(#stripLeft)" role="img" aria-label="Film strip showing a wedding couple with flowers"/>
  <polygon points="596,148 784,128 784,280 596,290" fill="url(#stripRight)" role="img" aria-label="Film strip showing children at a birthday party"/>
  <rect x="165" y="107" width="428" height="243" rx="6" fill="#3a3a3a"/>
  <rect x="178" y="120" width="402" height="194" fill="url(#screen)" role="img" aria-label="Video still of a casket covered in flowers"/>
  <polygon points="374,197 374,237 406,217" fill="#fff"/>
  <rect x="178" y="314" width="402" height="28" fill="#1c1c1c"/>
  <rect x="178" y="316" width="402" height="3" fill="#555"/>
  <circle cx="182" cy="318" r="4" fill="#ddd"/>
  <rect x="189" y="326" width="2.5" height="8" fill="#ccc"/><rect x="194" y="326" width="2.5" height="8" fill="#ccc"/>
  <polygon points="214,328 218,328 222,325 222,335 218,332 214,332" fill="#ccc"/>
  <text x="233" y="333" fill="#ccc" font-size="6.5" font-family="Arial">00:00 / 18:50</text>
  <circle cx="495" cy="330" r="3.5" fill="none" stroke="#ccc" stroke-width="1.5"/>
  <circle cx="514" cy="330" r="3" fill="#ccc"/>
  <rect x="526" y="326" width="9" height="7" fill="none" stroke="#fff" stroke-width="1.5"/>
  <rect x="545" y="326" width="11" height="7" fill="none" stroke="#ccc" stroke-width="1"/>
  <rect x="565" y="325" width="9" height="9" fill="none" stroke="#ccc" stroke-width="1" stroke-dasharray="3 3"/>
</svg>

<div class="abs logo"><span class="logo-mark"></span><span class="logo-name">Reel Keepsake</span></div>
<div class="abs social" aria-label="Social links"><span></span><span></span><span></span><span></span><span></span></div>
<nav class="abs nav"><a href="#">Home</a><a href="#">About</a><a href="#">Services</a><a href="#">Packages</a><a href="#">Samples</a><a href="#">FAQ</a><a href="#">Contact</a></nav>

<h1 class="abs tagline">Putting together Videos and Photos with music<br>to show wonderful presentation</h1>
<p class="abs intro">Lorem ipsum dolor sit amet, consectetur adipisicing elit, sed do eiusmod tempor incididunt ut labore et dolore magna aliqua. Ut enim ad minim veniam, quis nostrud exercitation ullamco laboris nisi ut aliquip ex ea commodo consequat. Duis aute irure dolor in reprehenderit in voluptate velit esse cillum dolore eu fugiat nulla pariatur. Excepteur sint occaecat cupidatat non proident, sunt in culpa qui officia deserunt mollit anim id est laborum.</p>

<section class="abs occasions">
  <h2 class="section-title">We do presentation for the following occasions:</h2>
  <div class="card" style="left:25px">
    <div class="photo" style="background:linear-gradient(#7d9a5a,#c98a9a)" role="img" aria-label="Flower-covered casket"></div>
    <h3>FUNERAL</h3>
    <p>Lorem ipsum dolor sit amet, consectetur adipisicing elit, sed do eiusmod tempor incididunt ut labore et dolore magna aliqua.</p>
    <span class="inquire">inquire</span>
  </div>
  <div class="card" style="left:209px">
    <div class="photo" style="background:linear-gradient(#cfc7bf,#8a8f97)" role="img" aria-label="Bride and groom embracing"></div>
    <h3 style="margin-left:5px">WEDDING</h3>
    <p style="margin-left:5px">Ut enim ad minim veniam, quis nostrud exercitation ullamco laboris nisi ut aliquip ex ea commodo consequat.</p>
    <span class="inquire" style="margin-left:5px">inquire</span>
  </div>
  <div class="card" style="left:393px">
    <div class="photo" style="background:linear-gradient(#d2a070,#c8504a)" role="img" aria-label="Children celebrating a birthday"></div>
    <h3 style="margin-left:5px">BIRTHDAY</h3>
    <p style="margin-left:5px">Duis aute irure dolor in reprehenderit in voluptate velit esse cillum dolore eu fugiat nulla pariatur. Excepteur sint occaecat cupidatat non proident,</p>
    <span class="inquire" style="margin-left:5px">inquire</span>
  </div>
  <div class="card" style="left:577px">
    <div class="photo" style="background:linear-gradient(#6f7a5a,#2a2a2a)" role="img" aria-label="Graduates in caps and gowns"></div>
    <h3 style="margin-left:7px">OTHERS</h3>
    <p style="margin-left:9px">Sunt in culpa qui officia deserunt mollit anim id est laborum.  voluptate velit esse cillum dolore eu fugiat nulla pariatur. Excepteur sint occaecat cupidatat non</p>
    <span class="inquire" style="margin-left:9px">inquire</span>
  </div>
</section>

<section class="abs testimonials">
  <h2 class="section-title">Testimonials</h2>
  <div class="quote">
    <svg class="icon" width="32" height="26" viewBox="0 0 32 26"><ellipse cx="14" cy="11" rx="13" ry="9" fill="#4a7fd0"/><ellipse cx="20" cy="15" rx="11" ry="8" fill="#2d62b8"/><polygon points="10,18 6,25 16,19" fill="#4a7fd0"/></svg>
    <p class="lead">They are very professional and thrustworthy. No need for supervision while they are on work.</p>
    <p class="body">My guests love the presentation and they were touched. The music combined photos and music are frantastic. The story telling is well organized. I highly reccommend<br>Reel Keepsake</p>
    <p class="by">by: Mara Ellison</p>
  </div>
  <div class="quote-rule"></div>
  <div class="quote">
    <svg class="icon" width="32" height="26" viewBox="0 0 32 26"><ellipse cx="14" cy="11" rx="13" ry="9" fill="#4a7fd0"/><ellipse cx="20" cy="15" rx="11" ry="8" fill="#2d62b8"/><polygon points="10,18 6,25 16,19" fill="#4a7fd0"/></svg>
    <p class="lead">They are very professional and thrustworthy. No need for supervision while they are on work.</p>
    <p class="body">My guests love the presentation and they were touched. The music combined photos and music are frantastic. The story telling is well organized. I highly reccommend<br>Reel Keepsake</p>
    <p class="by">by: Mara Ellison</p>
  </div>
</section>

<section class="abs news">
  <h2 class="section-title">News and Promos</h2>
  <div class="news-list">
    <div class="news-item">
      <div class="date"><b>27</b><small>JULY</small></div>
      <div class="news-body"><h4>Lorem ipsum dolor sit amet</h4>consectetur adipisicing elit, sed do eiusmod tempor incididunt ut labore et dolore magna aliqua.<span class="more">read more</span></div>
    </div>
    <div class="news-item">
      <div class="date"><b>24</b><small>JULY</small></div>
      <div class="news-body"><h4>Lorem ipsum dolor sit amet</h4>consectetur adipisicing elit, sed do eiusmod tempor incididunt ut labore et dolore magna aliqua.<span class="more">read more</span></div>
    </div>
    <div class="news-item">
      <div class="date"><b>15</b><small>JULY</small></div>
      <div class="news-body"><h4>Lorem ipsum dolor sit amet</h4>consectetur adipisicing elit, sed do eiusmod tempor incididunt ut labore et dolore magna aliqua.<span class="more">read more</span></div>
    </div>
  </div>
</section>

<footer class="abs footer">
  <p class="links">ABOUT US · SERVICES · PACKAGES · SAMPLES · FAQ · CONTACT US</p>
  <p class="copy">© Copyright 2013 Northbay Studio. All Rights Reserved</p>
</footer>
</body>
</html>
```